Korlu - coded wordpress homepage needed for modern real estate business

I need a one page website created for Korlu a cutting edge real estate agency. Please read the must haves for more information on the design. The website must be created into a wordpress theme and the winning designer must install wordpress and the site into my hosting included as part of this project. The site must also be secure and perform well with optimised images etc.

Ongoing work is available for the right person. More instructions include the website sections/content can be found here https://files.plimbrodocs.net/page/d/7TkRwPzqLmNa3_b58HjVuYesZd-K4pLCxBnWoFqTgRSE/view?mode=shared

Coding

Coded - Design and coding required

Colors

Designer to choose colors to be used in the design.

Requirements
Must have
• The project must be a modern, cutting edge website created in a similar style to leading modern brands. It must have flat graphics and look very good. Most real estate websites are not very good and I want this website to be the best in the industry.
• It must also be responsive and look good on mobile as well as desktop. Please make desktop versions first and if you are likely to be the designer I choose then I will get you to make up a mobile mock up once the website is almost done. Please design the site however you feel best and I will provide feedback from there. I am getting the logo created at the moment in another design competition so please use a mock logo for now and when the logo is finalised I will upload it in this brief. The logo will be white/red and the colour palette of the website needs to be dark. The red colour used must be #e60611 or CMYK C - 3% M - 100% Y - 100% K - 1% or RGB R - 230 G - 6 B - 17.
• Any questions just ask me, look forward to seeing your designs

```html
<!DOCTYPE html>
<html lang="en">
<head>
<meta charset="utf-8">
<title>Korlu Realestate</title>
<link href="https://fonts.googleapis.com/css2?family=Noto+Serif:wght@400;700&family=Montserrat:wght@400;500;600&display=swap" rel="stylesheet">
<style>
:root{
  --bg:#061316;
  --bg-soft:#0b1b1f;
  --red:#e60611;
  --white:#ffffff;
  --text:#e8ecec;
  --muted:#b9c2c4;
  --line:#6d7a7d;
  --ghost:rgba(255,255,255,0.07);
  --serif:'Noto Serif', Georgia, serif;
  --sans:'Montserrat', Arial, sans-serif;
}
*{box-sizing:border-box;margin:0;padding:0}
html,body{width:1200px;height:4587px;overflow:hidden}
body{background:var(--bg);color:var(--text);font-family:var(--sans);position:relative}
.abs{position:absolute}

/* header + hero */
.hero{left:0;top:0;width:1200px;height:600px;
  background:linear-gradient(180deg,#3e5561 0%,#54666a 10%,#3f5436 30%,#33452a 55%,#4e5a3a 80%,#6b6a4e 100%)}
.hero-river{left:0;top:130px;width:1200px;height:470px;
  background:linear-gradient(115deg,rgba(180,170,120,.35) 0%,rgba(180,170,120,.35) 6%,rgba(40,80,130,.75) 9%,rgba(40,80,130,.75) 13%,transparent 16%)}
.hero-shade{left:0;top:0;width:1200px;height:600px;background:linear-gradient(180deg,rgba(0,0,0,.35) 0%,rgba(0,0,0,0) 20%,rgba(0,0,0,.15) 100%)}
.nav{left:0;top:0;width:1200px;height:84px}
.nav a{position:absolute;top:30px;font-size:13px;color:var(--white);text-decoration:none;font-family:var(--sans)}
.nav .active{left:141px;top:0;width:60px;height:84px;background:var(--white);color:var(--red);text-align:center;padding-top:30px}
.brand{left:520px;top:52px;width:160px;text-align:center}
.brand-name{font-family:var(--serif);font-size:14px;font-weight:400;color:var(--white)}
.nav .cta{left:960px;top:23px;width:98px;height:36px;border:1.5px solid var(--white);border-radius:18px;text-align:center;line-height:33px;padding:0}
.hero-title{left:0;top:266px;width:1200px;text-align:center;font-family:var(--serif);font-weight:400;font-size:48px;color:var(--white)}
.hero-sub{left:0;top:332px;width:1200px;text-align:center;font-size:24px;line-height:41px;color:var(--white);font-weight:500}
.scroll-btn{left:564px;top:564px;width:72px;height:72px;border-radius:50%;background:var(--white);border:4px solid var(--bg)}

/* section headings */
.sec-head{left:0;width:1200px;text-align:center}
.sec-head .ghost{position:absolute;left:0;width:1200px;top:-22px;font-family:var(--serif);font-size:68px;color:var(--ghost);text-align:center}
.sec-head h2{position:relative;font-family:var(--serif);font-weight:400;font-size:34px;color:var(--white)}
.bar{display:block;width:44px;height:2px;background:var(--red);margin:10px auto 0}

/* appraisal */
.appraisal-head{left:142px;top:712px}
.appraisal-head .ghost{position:absolute;left:150px;top:10px;font-family:var(--serif);font-size:70px;color:var(--ghost)}
.appraisal-head h2{position:relative;font-family:var(--serif);font-weight:400;font-size:33px;line-height:39px;color:var(--white)}
.appraisal-head .bar{margin:14px 0 0}
.ticks{list-style:none}
.ticks li{position:absolute;left:0;font-size:12px;color:var(--text);padding-left:17px;white-space:nowrap;line-height:17px}
.ticks li::before{content:"";position:absolute;left:0;top:4px;width:7px;height:7px;border:1.5px solid var(--text);border-radius:50%}
.contact-box{left:635px;top:707px;width:424px;height:236px;border:1.5px solid var(--line);border-radius:3px}
.contact-box h3{position:absolute;left:0;top:18px;width:100%;text-align:center;font-family:var(--serif);font-weight:400;font-size:20px;color:var(--white)}
.field{position:absolute;height:34px;border:1.5px solid var(--line);border-radius:17px;font-size:10px;color:var(--muted);padding:11px 18px}
.btn-red{position:absolute;background:var(--red);color:var(--white);border-radius:17px;text-align:center;font-size:12px}

/* different */
.diff-frame{left:119px;top:1141px;width:395px;height:351px;border:1.5px solid var(--line);border-radius:3px}
.photo{border-radius:3px}
.diff-photo{left:141px;top:1118px;width:395px;height:352px;background:linear-gradient(160deg,#e9e4dc 0%,#d7cfc2 40%,#b5a694 70%,#8e8070 100%)}
.values{left:570px;top:1126px;width:500px}
.value{position:absolute;left:0;width:490px}
.value h4{font-family:var(--serif);font-weight:400;font-size:14px;color:var(--white);padding-left:18px;position:relative}
.value h4::before{content:"";position:absolute;left:0;top:5px;width:7px;height:7px;border:1.5px solid var(--white);border-radius:50%}
.value.on h4{color:var(--red)}
.value.on h4::before{border-color:var(--red)}
.value p{font-size:11px;line-height:18px;color:var(--text);padding-left:18px;margin-top:6px}

/* marketing */
.mkt{left:142px;width:490px}
.mkt h4{font-family:var(--serif);font-weight:400;font-size:14px;color:var(--white)}
.mkt-line{left:142px;top:1769px;width:485px;height:1px;background:var(--line)}
.mkt-list li{font-size:11px;white-space:normal;width:470px}
.mkt-frame{left:685px;top:1670px;width:394px;height:352px;border:1.5px solid var(--line);border-radius:3px}
.mkt-photo{left:662px;top:1648px;width:396px;height:353px;background:radial-gradient(circle at 40% 55%,#9aa0a0 0%,#6c7564 30%,#3f5a34 60%,#2c4325 100%)}

/* cards */
.card{width:289px;height:374px;border:1.5px solid var(--line);border-radius:3px;background:var(--bg)}
.card .img{position:absolute;left:10px;top:10px;width:266px;height:210px;background:linear-gradient(180deg,#7a99b5 0%,#a8b4b2 22%,#3d5a33 40%,#445c34 70%,#c2ad82 100%)}
.card .img.b{background:linear-gradient(180deg,#8aa4bb 0%,#4e6b3f 30%,#3a5530 65%,#55683d 100%)}
.card .img.c{background:linear-gradient(180deg,#a7b2a3 0%,#7d8a58 35%,#5a7040 70%,#4c6337 100%)}
.card h5{position:absolute;left:14px;font-family:var(--serif);font-weight:400;font-size:13.5px;color:var(--white)}
.card p{position:absolute;left:16px;width:260px;font-size:11px;line-height:18px;color:var(--text)}
.spec{position:absolute;font-size:11px;color:var(--text);display:flex;align-items:center;gap:8px}
.price{position:absolute;left:16px;font-size:11px;color:var(--white)}
.arrow{width:36px;height:36px;border-radius:50%;border:1.5px solid var(--white)}
.arrow.next{background:var(--red);border-color:var(--red)}
.arrow svg{position:absolute;left:12px;top:11px}
.who{position:absolute;left:14px;display:flex;align-items:center;gap:10px;font-family:var(--serif);font-size:14px;color:var(--white)}
.who i{display:block;width:26px;height:26px;border-radius:50%;background:#b08a72;border:2px solid var(--white)}
.date{position:absolute;right:14px;font-size:11px;color:var(--text);display:flex;align-items:center;gap:6px}

/* testimonial */
.avatar{border-radius:50%;border:3px solid var(--white)}
.quote-name{left:0;top:2790px;width:1200px;text-align:center;font-size:14px;font-weight:600;color:var(--white)}
.quote{left:338px;top:2820px;width:524px;text-align:center;font-size:11px;line-height:18px;color:var(--text)}
.dot{width:11px;height:11px;border-radius:50%;border:1.5px solid var(--white)}
.dot.on{border-color:var(--red);background:radial-gradient(circle,var(--red) 0 40%,transparent 45%)}

/* team */
.video{height:282px;border:1.5px solid var(--line);border-radius:3px}
.video.a{left:142px;top:3081px;width:447px;background:linear-gradient(180deg,#c5cfd6 0%,#8d8f85 40%,#3e4345 70%,#707a6a 100%)}
.video.b{left:611px;top:3081px;width:447px;background:linear-gradient(180deg,#e0e4e3 0%,#b8b4a8 40%,#6e7060 70%,#9a9c92 100%)}
.play{position:absolute;left:50%;top:50%;width:46px;height:32px;margin:-16px 0 0 -23px;border:2.5px solid var(--white);border-radius:9px}
.play::after{content:"";position:absolute;left:16px;top:7px;border-left:12px solid var(--white);border-top:7px solid transparent;border-bottom:7px solid transparent}
.member{top:3378px;width:447px;text-align:center}
.member h4{font-family:var(--serif);font-weight:400;font-size:20px;color:var(--white)}
.member span{font-size:11px;color:var(--text)}

/* inquiry */
.inquiry{left:0;top:4019px;width:1200px;height:494px;background:radial-gradient(ellipse at 50% 40%,#2e302f 0%,#1d1f1f 55%,#111414 100%)}
.inq-title{left:0;top:4110px;width:1200px;text-align:center;font-family:var(--serif);font-weight:400;font-variant:small-caps;font-size:30px;color:var(--white);letter-spacing:1px}
.inq-title em{font-style:normal;color:var(--red)}
.inq-field{position:absolute;background:var(--white);border-radius:2px;font-size:11px;color:#777;padding:10px 14px;height:36px}
.inq-submit{left:552px;top:4400px;width:94px;height:30px;border:1.5px solid var(--white);border-radius:15px;font-size:12px;color:var(--white);display:flex;align-items:center;justify-content:center;gap:6px}

/* footer */
.footer{left:0;top:4513px;width:1200px;height:74px;background:var(--red)}
.footer-name{left:146px;top:4530px;font-family:var(--serif);font-weight:400;font-size:30px;color:var(--white);letter-spacing:1px}
.footer-copy{left:700px;top:4542px;width:356px;text-align:right;font-size:12px;color:var(--white)}
</style>
</head>
<body>

<!-- Header and hero -->
<section class="hero abs" role="img" aria-label="Aerial photo of a river winding through forested valley"></section>
<div class="hero-river abs"></div>
<div class="hero-shade abs"></div>
<nav class="nav abs">
  <a class="active" href="#">Home</a>
  <a href="#" style="left:213px">Appraisal</a>
  <a href="#" style="left:296px">Different</a>
  <a href="#" style="left:375px">Specialty</a>
  <a href="#" style="left:455px">Market</a>
  <a href="#" style="left:702px">Testimonial</a>
  <a href="#" style="left:797px">Team</a>
  <a href="#" style="left:853px">Sold</a>
  <a href="#" style="left:903px">About</a>
  <a class="cta" href="#">Contact Us</a>
</nav>
<div class="brand abs"><span class="brand-name">Korlu Realestate</span></div>
<h1 class="hero-title abs">Real Estate Done Differently</h1>
<p class="hero-sub abs">We Are Exceptional In Everything We Do So You Can<br>Have Confidence Depending On Us</p>
<div class="scroll-btn abs">
  <svg class="abs" style="left:24px;top:22px" width="16" height="20" viewBox="0 0 16 20" fill="none" stroke="#061316" stroke-width="2"><path d="M2 3l6 6 6-6M2 10l6 6 6-6"/></svg>
</div>

<!-- Appraisal -->
<div class="appraisal-head abs">
  <span class="ghost">Appraisal</span>
  <h2>Organise a Free<br>Market Appraisal</h2>
  <span class="bar"></span>
</div>
<ul class="ticks abs" style="left:142px;top:826px">
  <li style="top:0">Get a current price indication and market update</li>
  <li style="top:26px">Learn more on the process of selling your property with us</li>
  <li style="top:54px">100% free with no hidden costs and absolutely no pressure or sales tactics</li>
  <li style="top:84px">Meet with us face to face and ask us anything</li>
</ul>
<form class="contact-box abs">
  <h3>Contact Now</h3>
  <span class="field" style="left:22px;top:73px;width:183px">First Name</span>
  <span class="field" style="left:219px;top:73px;width:183px">Last Name</span>
  <span class="field" style="left:22px;top:123px;width:183px">Phone Number</span>
  <span class="field" style="left:219px;top:123px;width:183px">Email Address</span>
  <span class="btn-red" style="left:161px;top:178px;width:98px;height:34px;line-height:34px">Submit</span>
</form>

<!-- How we're different -->
<div class="sec-head abs" style="top:1022px"><span class="ghost">Different</span><h2>How We’re Different</h2><span class="bar"></span></div>
<div class="diff-frame abs"></div>
<div class="diff-photo photo abs" role="img" aria-label="Family relaxing together on a sofa in a bright living room"></div>
<div class="values abs">
  <div class="value" style="top:0"><h4>Integrity</h4><p>We are honest, reliable and trustworthy. We truly value all our clients and will go above and beyond.</p></div>
  <div class="value on" style="top:69px"><h4>Exclusive</h4><p>We only take on a small number of listings every month to ensure we deliver a high standard of service to every single one of our clients.</p></div>
  <div class="value" style="top:139px"><h4>Location</h4><p>We ONLY sell properties in Ashbury Vale, Linden Ridge and Fernhill giving us an intimate knowledge of the market and area.</p></div>
  <div class="value" style="top:208px"><h4>Technology</h4><p>We utilise the latest technology in the real estate industry to enhance our capabilities and get the best possible results.</p></div>
  <div class="value" style="top:277px"><h4>Local</h4><p>We have been Greystone Ranges locals for over 25 years and are always only a phone call away or 5 minutes down the road if you would like to meet with us.</p></div>
</div>

<!-- Marketing -->
<div class="sec-head abs" style="top:1572px"><span class="ghost">Specialty</span><h2>Marketing Is Our Specialty</h2><span class="bar"></span></div>
<div class="mkt abs" style="top:1654px"><h4>Our marketing will supercharge the sale of your property by</h4></div>
<ul class="ticks mkt-list abs" style="left:142px;top:1683px">
  <li style="top:0">Creating more enquiries and therefore more prospective buyers</li>
  <li style="top:25px">Putting you in a better negotiating position by having more prospective buyers</li>
  <li style="top:50px">Giving you the best chance to maximise the sale price of your property</li>
</ul>
<div class="mkt-line abs"></div>
<div class="mkt abs" style="top:1787px"><h4>This is achieved through our innovative marketing strategies including</h4></div>
<ul class="ticks mkt-list abs" style="left:142px;top:1815px">
  <li style="top:0">Use of the industry leading Customer Relationship Manager (CRM) Software as used by 40% of the country’s Top 100 Agents</li>
  <li style="top:48px">Use of drones, professional videography and Chatterly marketing</li>
  <li style="top:75px">Top quality prospective buyer follow up and logging through utilising the capabilities of the CRM</li>
  <li style="top:114px">Email marketing specifically via buyer matching from our database</li>
  <li style="top:139px">Keeping our vendors regularly updated through weekly reports to enable informed decision making</li>
  <li style="top:182px">We also offer all traditional marketing strategies at a very high standard</li>
</ul>
<div class="mkt-frame abs"></div>
<div class="mkt-photo photo abs" role="img" aria-label="Aerial view of a suburban neighbourhood among trees"></div>

<!-- On the market -->
<div class="sec-head abs" style="top:2101px"><span class="ghost">Market</span><h2>On The Market</h2><span class="bar"></span></div>
<div class="arrow abs" style="left:85px;top:2346px"><svg width="10" height="12" viewBox="0 0 10 12" fill="none" stroke="#fff" stroke-width="2"><path d="M7 1L2 6l5 5"/></svg></div>
<div class="arrow next abs" style="left:1079px;top:2346px"><svg width="10" height="12" viewBox="0 0 10 12" fill="none" stroke="#fff" stroke-width="2"><path d="M3 1l5 5-5 5"/></svg></div>

<article class="card abs" style="left:142px;top:2179px">
  <div class="img" role="img" aria-label="Aerial photo of a river valley"></div>
  <h5 style="top:236px">Property Name Lorem Ipsum.</h5>
  <p style="top:260px">Lorem Ipsum is simply dummy text of the printing and typesetting industry.</p>
  <span class="spec" style="left:16px;top:306px"><svg width="20" height="20" viewBox="0 0 20 20" fill="none" stroke="#fff" stroke-width="1.3"><rect x="2" y="2" width="16" height="16" stroke-dasharray="3 2"/></svg>950 Sq Ft</span>
  <span class="spec" style="left:118px;top:306px"><svg width="22" height="20" viewBox="0 0 22 20" fill="none" stroke="#fff" stroke-width="1.3"><path d="M2 19h18M5 19V9h5v10M10 19V4h7v15M7 12h1M13 8h1M13 12h1"/></svg>Property Location</span>
  <span class="price" style="top:342px">For Sale :- $540,000</span>
</article>
<article class="card abs" style="left:456px;top:2179px">
  <div class="img b" role="img" aria-label="Aerial photo of forested hills"></div>
  <h5 style="top:236px">Property Name Lorem Ipsum.</h5>
  <p style="top:260px">Lorem Ipsum is simply dummy text of the printing and typesetting industry.</p>
  <span class="spec" style="left:16px;top:306px"><svg width="20" height="20" viewBox="0 0 20 20" fill="none" stroke="#fff" stroke-width="1.3"><rect x="2" y="2" width="16" height="16" stroke-dasharray="3 2"/></svg>1000 Sq Ft</span>
  <span class="spec" style="left:118px;top:306px"><svg width="22" height="20" viewBox="0 0 22 20" fill="none" stroke="#fff" stroke-width="1.3"><path d="M2 19h18M5 19V9h5v10M10 19V4h7v15M7 12h1M13 8h1M13 12h1"/></svg>Property Location</span>
  <span class="price" style="top:342px">For Sale :- $840,000</span>
</article>
<article class="card abs" style="left:769px;top:2179px">
  <div class="img c" role="img" aria-label="Aerial photo of a golf course among trees"></div>
  <h5 style="top:236px">Property Name Lorem Ipsum.</h5>
  <p style="top:260px">Lorem Ipsum is simply dummy text of the printing and typesetting industry.</p>
  <span class="spec" style="left:16px;top:306px"><svg width="20" height="20" viewBox="0 0 20 20" fill="none" stroke="#fff" stroke-width="1.3"><rect x="2" y="2" width="16" height="16" stroke-dasharray="3 2"/></svg>350 Sq Ft</span>
  <span class="spec" style="left:118px;top:306px"><svg width="22" height="20" viewBox="0 0 22 20" fill="none" stroke="#fff" stroke-width="1.3"><path d="M2 19h18M5 19V9h5v10M10 19V4h7v15M7 12h1M13 8h1M13 12h1"/></svg>Property Location</span>
  <span class="price" style="top:342px">For Sale :- $240,000</span>
</article>

<!-- Testimonial -->
<div class="sec-head abs" style="top:2632px"><span class="ghost">Testimonial</span><h2>What Our Clients Say</h2><span class="bar"></span></div>
<div class="avatar abs" style="left:474px;top:2713px;width:56px;height:56px;background:#c9a58a" role="img" aria-label="Client portrait"></div>
<div class="avatar abs" style="left:564px;top:2705px;width:72px;height:72px;background:#a86f5c" role="img" aria-label="Client portrait"></div>
<div class="avatar abs" style="left:670px;top:2713px;width:56px;height:56px;background:#8f7a6c" role="img" aria-label="Client portrait"></div>
<p class="quote-name abs">Sam Lorne</p>
<p class="quote abs">Lorem Ipsum is simply dummy text of the printing and typesetting industry. Lorem Ipsum has been the industry's standard dummy text ever since the 1500s, when an unknown printer took a galley of type and scrambled it to make a type specimen book. It has survived not only typesetting, remaining essentially unchanged.</p>
<span class="dot abs" style="left:572px;top:2913px"></span>
<span class="dot on abs" style="left:594px;top:2913px"></span>
<span class="dot abs" style="left:617px;top:2913px"></span>

<!-- Team -->
<div class="sec-head abs" style="top:3004px"><span class="ghost">Team</span><h2>Meet The Team</h2><span class="bar"></span></div>
<div class="video a abs" role="img" aria-label="Video still of an agent walking with a client between apartment buildings"><span class="play"></span></div>
<div class="video b abs" role="img" aria-label="Video still of an agent meeting a couple outside a home"><span class="play"></span></div>
<div class="member abs" style="left:142px"><h4>Nora Whitfield</h4><span>Licensee In Charge</span></div>
<div class="member abs" style="left:611px"><h4>Owen Pryce</h4><span>Sales Agent</span></div>

<!-- Recently sold -->
<div class="sec-head abs" style="top:3496px"><span class="ghost">Sold</span><h2>Recently Sold</h2><span class="bar"></span></div>
<div class="arrow abs" style="left:85px;top:3741px"><svg width="10" height="12" viewBox="0 0 10 12" fill="none" stroke="#fff" stroke-width="2"><path d="M7 1L2 6l5 5"/></svg></div>
<div class="arrow next abs" style="left:1079px;top:3741px"><svg width="10" height="12" viewBox="0 0 10 12" fill="none" stroke="#fff" stroke-width="2"><path d="M3 1l5 5-5 5"/></svg></div>

<article class="card abs" style="left:142px;top:3573px">
  <div class="img" role="img" aria-label="Aerial photo of a river valley"></div>
  <span class="who" style="top:237px"><i role="img" aria-label="Agent portrait"></i>Sam Lorne</span>
  <span class="date" style="top:244px"><svg width="13" height="13" viewBox="0 0 13 13" fill="none" stroke="#fff" stroke-width="1.2"><rect x="1" y="2" width="11" height="10"/><path d="M1 5h11M4 1v2M9 1v2"/></svg>July 13, 2019</span>
  <h5 style="top:274px">Property Name Lorem Ipsum.</h5>
  <span class="spec" style="left:16px;top:306px"><svg width="20" height="20" viewBox="0 0 20 20" fill="none" stroke="#fff" stroke-width="1.3"><rect x="2" y="2" width="16" height="16" stroke-dasharray="3 2"/></svg>950 Sq Ft</span>
  <span class="spec" style="left:118px;top:306px"><svg width="22" height="20" viewBox="0 0 22 20" fill="none" stroke="#fff" stroke-width="1.3"><path d="M2 19h18M5 19V9h5v10M10 19V4h7v15M7 12h1M13 8h1M13 12h1"/></svg>Property Location</span>
  <span class="price" style="top:342px">Sold :- $540,000</span>
</article>
<article class="card abs" style="left:456px;top:3573px">
  <div class="img" role="img" aria-label="Aerial photo of a river valley"></div>
  <span class="who" style="top:237px"><i role="img" aria-label="Agent portrait"></i>Sam Lorne</span>
  <span class="date" style="top:244px"><svg width="13" height="13" viewBox="0 0 13 13" fill="none" stroke="#fff" stroke-width="1.2"><rect x="1" y="2" width="11" height="10"/><path d="M1 5h11M4 1v2M9 1v2"/></svg>July 13, 2019</span>
  <h5 style="top:274px">Property Name Lorem Ipsum.</h5>
  <span class="spec" style="left:16px;top:306px"><svg width="20" height="20" viewBox="0 0 20 20" fill="none" stroke="#fff" stroke-width="1.3"><rect x="2" y="2" width="16" height="16" stroke-dasharray="3 2"/></svg>950 Sq Ft</span>
  <span class="spec" style="left:118px;top:306px"><svg width="22" height="20" viewBox="0 0 22 20" fill="none" stroke="#fff" stroke-width="1.3"><path d="M2 19h18M5 19V9h5v10M10 19V4h7v15M7 12h1M13 8h1M13 12h1"/></svg>Property Location</span>
  <span class="price" style="top:342px">Sold :- $540,000</span>
</article>
<article class="card abs" style="left:769px;top:3573px">
  <div class="img" role="img" aria-label="Aerial photo of a river valley"></div>
  <span class="who" style="top:237px"><i role="img" aria-label="Agent portrait"></i>Sam Lorne</span>
  <span class="date" style="top:244px"><svg width="13" height="13" viewBox="0 0 13 13" fill="none" stroke="#fff" stroke-width="1.2"><rect x="1" y="2" width="11" height="10"/><path d="M1 5h11M4 1v2M9 1v2"/></svg>July 13, 2019</span>
  <h5 style="top:274px">Property Name Lorem Ipsum.</h5>
  <span class="spec" style="left:16px;top:306px"><svg width="20" height="20" viewBox="0 0 20 20" fill="none" stroke="#fff" stroke-width="1.3"><rect x="2" y="2" width="16" height="16" stroke-dasharray="3 2"/></svg>950 Sq Ft</span>
  <span class="spec" style="left:118px;top:306px"><svg width="22" height="20" viewBox="0 0 22 20" fill="none" stroke="#fff" stroke-width="1.3"><path d="M2 19h18M5 19V9h5v10M10 19V4h7v15M7 12h1M13 8h1M13 12h1"/></svg>Property Location</span>
  <span class="price" style="top:342px">Sold :- $540,000</span>
</article>

<!-- Quick inquiry -->
<section class="inquiry abs" role="img" aria-label="Dark monochrome aerial photo of forest"></section>
<h2 class="inq-title abs"><em>Quick</em> Inquiry</h2>
<span class="bar abs" style="left:578px;top:4170px;margin:0"></span>
<span class="inq-field" style="left:255px;top:4196px;width:336px">First Name</span>
<span class="inq-field" style="left:609px;top:4196px;width:335px">Last Name</span>
<span class="inq-field" style="left:255px;top:4247px;width:336px">Mobile Number</span>
<span class="inq-field" style="left:609px;top:4247px;width:335px">Email</span>
<span class="inq-field" style="left:255px;top:4297px;width:689px;height:68px">Message</span>
<span class="inq-submit abs">SUBMIT <svg width="7" height="9" viewBox="0 0 7 9"><path d="M0 0l7 4.5L0 9z" fill="#fff"/></svg></span>

<!-- Footer -->
<footer class="footer abs"></footer>
<span class="footer-name abs">KORLU</span>
<span class="footer-copy abs">Copyright © 2019 Korlu. All Rights Reserved.</span>

</body>
</html>
```